Wealth Management Business Card

We are a professional services consulting firm that specializes in high net worth individuals over $25,000,000, executives C-suite and above, closely held businesses owners, family offices and highly compensated employees.

Our focus is on risk mitigation and tax efficient strategies. Our clients take their risk on themselves and have a proven track record generating wealth. Our directive is to preserve and protect the wealth they’ve already created.

Our company Harbridge Advisory is geared around five directives of asset protection:
1) Legal Structuring
2) Leverage & Financing
3) Risk Management - Asset Protection & Insurance, Trustee Work
4) Asset Management & Investing - Under www.qelvantcapital.com
5) Tax Efficient Strategies

Our Company Mark is a Pentagon with a key in the middle. A pentagon is the most efficient defensive structure. Each point of a pentagon is equal distance front every point . Each side provides support to another and works together, which is the key to our clients success.

Our key colors are blue, black and silver.

We ‘re located in the Pacific Northwest with bi coastal and international clients. We have fewer, higher net worth clients and provide exceptional customer service. We do not do social media.

website is www.harbridgepath.com

Target Market(s)

High End Clients

Contact Information for Business Card

extra thick

Font styles to use
Serif

Requirements
Must have
• Metalic foil for lettering.
Black Background on one side
White Background on the other
Horizontal Format Only
No Rounded corners
Not Marketing sales information on the card.
Nice to have
• imprinted texture on the card
Should not have
• lots of color

```html
<!DOCTYPE html>
<html lang="en">
<head>
<meta charset="utf-8">
<title>Harbridge Advisory – Business Card</title>
<link href="https://fonts.googleapis.com/css2?family=Cinzel:wght@500;600&family=Cormorant+Garamond:wght@500;600;700&display=swap" rel="stylesheet">
<style>
  :root{
    --bg:#e9ebee;
    --card-light:#ffffff;
    --card-dark:#0d0e10;
    --navy:#0b3f8a;
    --sky:#2f8fd2;
    --silver:#c9ccd1;
    --silver-soft:#9ea3aa;
    --ink:#3f444c;
    --shadow:0 18px 40px rgba(20,30,50,.18), 0 3px 8px rgba(20,30,50,.12);
  }
  *{box-sizing:border-box;margin:0;padding:0}
  html,body{width:1200px;height:900px;overflow:hidden}
  body{background:var(--bg);font-family:"Cormorant Garamond",serif;position:relative}
  .card{position:absolute;width:640px;height:366px;box-shadow:var(--shadow)}
  .card--back{left:70px;top:60px;background:var(--card-dark)}
  .card--front{left:490px;top:474px;background:var(--card-light)}

  /* back side (black) */
  .back-brand{position:absolute;left:0;right:0;top:128px;display:flex;align-items:center;justify-content:center;gap:16px}
  .brand-square{display:block;width:24px;height:24px;background:var(--silver)}
  .brand-name{font-family:"Cinzel",serif;font-weight:600;letter-spacing:.08em;text-transform:uppercase}
  .card--back .brand-name{color:var(--silver);font-size:32px;line-height:1}
  .back-url{position:absolute;left:0;right:0;top:272px;text-align:center;color:var(--silver-soft);font-weight:600;font-size:19px;letter-spacing:.14em}

  /* front side (white) */
  .front-brand{position:absolute;left:30px;top:128px;width:280px;text-align:center}
  .front-brand .brand-square{margin:0 auto 20px;width:22px;height:22px;background:var(--navy)}
  .front-brand .brand-name{display:block;color:var(--navy);font-size:26px;line-height:1.2}
  .divider{position:absolute;left:326px;top:70px;width:2px;height:226px;background:linear-gradient(var(--sky),var(--navy))}
  .contact{position:absolute;left:360px;top:78px;width:260px}
  .person-name{color:var(--sky);font-weight:700;font-size:30px;line-height:1.1}
  .person-role{color:var(--navy);font-weight:600;font-size:21px;margin-top:2px}
  .contact-list{list-style:none;margin-top:24px}
  .contact-list li{display:flex;align-items:center;gap:12px;color:var(--ink);font-weight:600;font-size:16px;margin-bottom:10px;white-space:nowrap}
  .contact-list svg{width:16px;height:16px;flex:none;fill:none;stroke:var(--sky);stroke-width:1.8}
</style>
</head>
<body>
  <section class="card card--back">
    <div class="back-brand">
      <span class="brand-square"></span>
      <span class="brand-name">Harbridge Advisory</span>
    </div>
    <p class="back-url">www.harbridgepath.com</p>
  </section>

  <section class="card card--front">
    <div class="front-brand">
      <span class="brand-square"></span>
      <span class="brand-name">Harbridge<br>Advisory</span>
    </div>
    <div class="divider"></div>
    <div class="contact">
      <p class="person-name">Daniel Marsh</p>
      <p class="person-role">Manager</p>
      <ul class="contact-list">
        <li><svg viewBox="0 0 24 24"><path d="M6 3l3 4-2 2a12 12 0 0 0 8 8l2-2 4 3-2 3C10 21 3 14 3 6z"/></svg>555-014-2260</li>
        <li><svg viewBox="0 0 24 24"><rect x="3" y="6" width="18" height="12"/><path d="M3 6l9 7 9-7"/></svg>daniel.marsh@harbridgepath.com</li>
        <li><svg viewBox="0 0 24 24"><circle cx="12" cy="12" r="9"/><path d="M3 12h18M12 3c3 3 3 15 0 18M12 3c-3 3-3 15 0 18"/></svg>www.harbridgepath.com</li>
      </ul>
    </div>
  </section>
</body>
</html>
```